依頼詳細
「北辰年金事務研究連盟」の概要・活動内容等を紹介するパンフレットの作成です。パンフレットとはいえ、A4裏表の簡易版でOKです(ページ数2ページ)。全体として、固い厳粛なイメージが出ればよいかと思います。記載する文章等は添付ファイルのとおりですので、配置や色、デザイン等の作成をお願いします。アレンジはお任せします。
記載項目
北辰年金事務研究連盟/ごあいさつ/協議会概要/活動内容(原則、添付ファイルの通り)
サイズ
A4
ページ数
両面
希望イメージ
シンプル 複雑
単色 カラフル
暗い 明るい
日常 高級
遊び心 厳粛
未来的 伝統的
女性的 男性的
希望する色
青系、茶系、グレー系、全体のバランスがよければ必ずしも上記に拘らないです。
納品ファイル
• PNG形式 (.png)
補足説明
協議会のWEBサイトは以下です。
http://hokushin-renmei.net/
内容やイメージの参考にしてください。

やや硬いイメージを保ちつつ、シンプルで分かりやすいという点を判断基準として、選択いたしました。ありがとうございます。

この度は、多くのランサーの方からご提案いただき、大変ありがとうございます。改めて感謝申し上げます。
途中、修正依頼させていただいた方におかれましては、実際の選択ポイントからずれた内容で依頼してしまったこともあり、この点、お詫び申し上げます。(私以外の担当の意見も反映したことによるものです。何卒ご容赦ください。)
今後また案件が発生した際には、ご協力いただければ幸いです。
どうぞ宜しくお願いします。

```html
<!DOCTYPE html>
<html lang="ja">
<head>
<meta charset="utf-8">
<title>北辰年金事務研究連盟 活動内容・協議会概要</title>
<link href="https://fonts.googleapis.com/css2?family=Noto+Sans+JP:wght@400;500;700;900&display=swap" rel="stylesheet">
<style>
:root{
  --navy:#1c3767;
  --navy-dark:#13284d;
  --paper:#eeeeec;
  --paper-edge:#d9d9d6;
  --ink:#2e2e2e;
  --muted:#5a5a5a;
  --rule:#a9afba;
}
*{box-sizing:border-box;margin:0;padding:0}
html,body{width:846px;height:1200px;overflow:hidden}
body{font-family:"Noto Sans JP",sans-serif;color:var(--ink);
  background:radial-gradient(ellipse at 50% 40%,#f6f6f4 0%,var(--paper) 60%,var(--paper-edge) 100%)}
.page{position:relative;width:846px;height:1200px;padding:32px 48px}
.section-band{display:flex;align-items:center;height:40px;
  background:linear-gradient(90deg,var(--navy-dark),var(--navy) 40%,rgba(28,55,103,.15));
  color:#fff;font-weight:700;font-size:19px;letter-spacing:.12em;padding-left:16px;border-radius:3px}
.activities{margin-top:26px}
.activity{margin-bottom:26px}
.activity-title{display:flex;align-items:baseline;color:var(--navy);font-weight:900;font-size:27px;letter-spacing:.02em;
  border-bottom:1px solid var(--rule);padding-bottom:6px}
.activity-num{font-style:italic;font-size:40px;margin-right:14px;line-height:1}
.activity-list{list-style:none;margin-top:10px;padding-left:14px}
.activity-list li{font-size:15px;line-height:26px;color:var(--ink)}
.activity-list li::before{content:"・"}
.overview{position:absolute;left:48px;right:48px;top:634px}
.overview-table{width:100%;border-collapse:collapse;margin-top:14px}
.overview-table th,.overview-table td{border-bottom:1px dotted var(--rule);padding:6px 4px;vertical-align:top;font-size:13.5px;line-height:20px}
.overview-table th{width:150px;text-align:justify;text-align-last:justify;color:var(--navy);font-weight:700;padding-right:26px}
.overview-table td{color:var(--ink)}
.small{font-size:11.5px;color:var(--muted)}
.site-url{position:absolute;left:0;right:0;bottom:26px;text-align:center;color:var(--navy);font-size:15px;letter-spacing:.08em;font-weight:500}
.site-url::before,.site-url::after{content:"";display:inline-block;width:200px;height:1px;background:var(--rule);vertical-align:middle;margin:0 16px}
</style>
</head>
<body>
<main class="page">
  <div class="section-band">活動内容</div>

  <section class="activities">
    <article class="activity">
      <h2 class="activity-title"><span class="activity-num">1.</span>社会保険加入促進の啓蒙活動</h2>
      <ul class="activity-list">
        <li>協議会所属の顧問社会保険労務士によるセミナーの開催（自主開催）</li>
        <li>業界団体様向けのセミナー勉強会の開催</li>
        <li>その他最新情報の提供活動</li>
      </ul>
    </article>
    <article class="activity">
      <h2 class="activity-title"><span class="activity-num">2.</span>社会保険調査リスク診断のご提供</h2>
      <ul class="activity-list">
        <li>現状の社会保険上の問題点、将来的負担・法的リスクに関する診断サービス</li>
      </ul>
    </article>
    <article class="activity">
      <h2 class="activity-title"><span class="activity-num">3.</span>社会保険調査対応&amp;コンサルティング</h2>
      <ul class="activity-list">
        <li>国家資格保持者・社会保険調査対応の専門家として、的確な指示・指導の実施</li>
        <li>各企業様の実情を鑑みた、コンサルティングサービスのご提供</li>
      </ul>
    </article>
  </section>

  <section class="overview">
    <div class="section-band">協議会概要</div>
    <table class="overview-table">
      <tr><th>団体名</th><td>北辰年金事務研究連盟</td></tr>
      <tr><th>趣旨</th><td>社会保険（厚生年金保険・健康保険・介護保険・雇用保険・労災保険）の適正な加入を促進するとともに、事業主の皆様が安心して経営に専念できるよう、調査対応に関する正しい知識と情報を提供し、社会保険の専門家集団として企業と従業員双方の利益に資することを目的とした任意団体</td></tr>
      <tr><th>代表</th><td>北辰年金事務研究連盟 代表 / 社会保険労務士 代表取締役</td></tr>
      <tr><th>副代表</th><td>副代表（社会保険労務士）<br>副代表（社会保険労務士）北辰労務事務所 代表</td></tr>
      <tr><th>特別アドバイザー</th><td>特別顧問（社会保険労務士）<br><span class="small">元年金事務所 調査担当</span></td></tr>
      <tr><th>設立</th><td>2015年</td></tr>
      <tr><th>所属社会保険労務士</th><td>38名<span class="small">（2015年4月1日現在）</span></td></tr>
      <tr><th>事務局</th><td>北辰労務サポートセンター<br>株式会社ミナトワークスコンサルティング<br>〒060-0042 北海道札幌市中央区大通西7-17-14 5F<br><span class="small">運営担当 事務局長（社会保険労務士）</span><br>TEL 011-555-0142　　FAX 011-555-0143</td></tr>
    </table>
  </section>

  <p class="site-url">http://hokushin-renmei.net/</p>
</main>
</body>
</html>
```